Thorne Consulting, Business Cards for International Development Consultancy

I'm an independent consultant working in the international development sector. I work with small organisations in developing countries to help them develop their community based programs so that they can be internationally competitive. This means they need to work better with their own communities to deliver meaningful quality work and also improve the accountability of their work so that they can compete for international and domestic funding.

I like the idea of being a connector between community, local organisations and international best practice and back again (ie acknowledging that international best practice can learn a lot from community).

My surname is Thorne - so I'd like the logo to use the idea of web as a connector.

I work with people with sight impairments - would like my card to be useful for low vision (i.e. clear graphics, easy to read font) and no vision (i.e. brail).

Target Market(s)

international non-government organisations (i.e. harvestaid, bright futures trust, open horizons), Blue Anchor Relief Alliance, government (i.e. Australian Bureau of Overseas Partnerships, consulars), non government agencies,

Industry/Entity Type

Business

Contact Information for Business Card

International Development Consultant
Connecting International Development with Community

Kerry Thorne
Lead Consultant
Phone: +61 417 382519
Email: kthorne.consulting@mailvale.com

Font styles to use
Sans Serif

Colors
eaf1f7
85acd3
d3a5cc
0456a4
a64599
0255a3

Requirements
Nice to have
• brail
Should not have
• fancy fonts - needs to be easy to read.

```html
<!DOCTYPE html>
<html lang="en">
<head>
<meta charset="utf-8">
<title>Kerry Thorne – Business Card</title>
<link rel="stylesheet" href="https://fonts.googleapis.com/css2?family=Bebas+Neue&family=Raleway:wght@400&display=swap">
<style>
  :root {
    --card-blue: #87a5d2;
    --band-white: #ffffff;
    --brand-navy: #1f4ea1;
    --ink: #1e1e1e;
    --web-tone: #eef3f9;
  }
  html, body {
    margin: 0;
    padding: 0;
    width: 1200px;
    height: 695px;
    overflow: hidden;
    background: var(--card-blue);
  }
  .card {
    position: relative;
    width: 1200px;
    height: 695px;
    background: var(--card-blue);
    font-family: "Raleway", sans-serif;
    font-variant-numeric: lining-nums;
  }
  .web-mark {
    position: absolute;
    left: 321px;
    top: 0;
    width: 567px;
    height: 276px;
  }
  .tagline-band {
    position: absolute;
    left: 0;
    top: 298px;
    width: 1200px;
    height: 80px;
    background: var(--band-white);
    display: flex;
    flex-direction: column;
    align-items: center;
    justify-content: center;
  }
  .tagline {
    margin: 0;
    font-family: "Bebas Neue", sans-serif;
    font-size: 34px;
    line-height: 38px;
    color: var(--brand-navy);
    text-align: center;
    letter-spacing: 0.2px;
    transform: translateX(-1px);
  }
  .person-name {
    position: absolute;
    left: 376px;
    top: 407px;
    margin: 0;
    font-weight: 400;
    font-size: 82px;
    line-height: 90px;
    letter-spacing: 1px;
    color: var(--brand-navy);
  }
  .person-role {
    position: absolute;
    left: 379px;
    top: 485px;
    margin: 0;
    font-size: 41px;
    line-height: 50px;
    color: var(--band-white);
  }
  .contact-list {
    position: absolute;
    left: 299px;
    top: 552px;
    margin: 0;
    padding: 0;
    list-style: none;
  }
  .contact-item {
    display: flex;
    align-items: center;
    height: 50px;
    margin-bottom: 12px;
    font-size: 40px;
    color: var(--ink);
  }
  .contact-icon {
    width: 50px;
    height: 50px;
    margin-right: 25px;
    flex: none;
  }
</style>
</head>
<body>
  <main class="card">
    <svg class="web-mark" viewBox="0 0 567 276" role="img" aria-label="Spider web logo mark symbolising connection">
      <rect width="567" height="276" rx="40" fill="var(--web-tone)"/>
    </svg>

    <div class="tagline-band">
      <p class="tagline">International Development Consultant Connecting</p>
      <p class="tagline">International Development with Community</p>
    </div>

    <h1 class="person-name">KERRY THORNE</h1>
    <p class="person-role">Lead Consultant</p>

    <ul class="contact-list">
      <li class="contact-item">
        <svg class="contact-icon" viewBox="0 0 50 50" aria-hidden="true">
          <circle cx="25" cy="25" r="25" fill="var(--band-white)"/>
          <path d="M17 13c1.5-1 3-.6 3.8.8l2.3 4c.6 1.1.3 2.3-.6 3l-1.8 1.4c1.2 2.8 3.3 5 6 6.3l1.5-1.8c.8-.9 2-1.1 3-.5l4 2.4c1.3.8 1.6 2.4.7 3.7l-1.4 1.9c-1 1.3-2.7 1.9-4.3 1.4C22.5 33.6 16.4 27.5 14.4 19.8c-.4-1.6.2-3.3 1.5-4.3z" fill="var(--card-blue)"/>
        </svg>
        <span>+61 417 382519</span>
      </li>
      <li class="contact-item">
        <svg class="contact-icon" viewBox="0 0 50 50" aria-hidden="true">
          <circle cx="25" cy="25" r="25" fill="var(--band-white)"/>
          <rect x="12" y="16" width="26" height="18" rx="1.5" fill="none" stroke="var(--card-blue)" stroke-width="2.5"/>
          <path d="M13 17.5l12 9.5 12-9.5M13 33l9-7.5M37 33l-9-7.5" fill="none" stroke="var(--card-blue)" stroke-width="2.2"/>
        </svg>
        <span>kthorne.consulting@mailvale.com</span>
      </li>
    </ul>
  </main>
</body>
</html>
```